Korvane Sky Works, LLC - Business Card

I currently have a drone business that specializes in aerial photography, thermal image inspections, deer recovery, search and rescue, custom agricultural applications. i will attach my current business card as well as some logos to incorporate for a new up to date business card
Updates

Designs look the same

Sick

Target Market(s)

farmers, hunters

Contact Information for Business Card

name address phone number (as existing card i attached)

Requirements
Must have
• im good with existing business card, but would like an agricultural twist

```html
<!DOCTYPE html>
<html lang="en">
<head>
<meta charset="utf-8">
<title>Korvane Sky Works, LLC – Business Card</title>
<link rel="stylesheet" href="https://fonts.googleapis.com/css2?family=Arimo:wght@400;700&display=swap">
<style>
  :root {
    --canvas-bg: #e6e6e6;
    --card-light: #f6f6f6;
    --card-dark: #000000;
    --green: #4a9a25;
    --green-deep: #1f7a12;
    --green-bright: #5f9f2e;
    --ink: #222222;
    --ink-soft: #555555;
    --divider: #bdbdbd;
    --white: #ffffff;
  }
  * { box-sizing: border-box; margin: 0; padding: 0; }
  html, body {
    width: 1200px; height: 1040px; overflow: hidden;
    background: var(--canvas-bg);
    font-family: "Arimo", Arial, sans-serif;
  }
  .canvas { position: relative; width: 1200px; height: 1040px; }
  .card {
    position: absolute; left: 200px; width: 800px; height: 458px;
    border-radius: 22px; overflow: hidden;
  }
  .card--front { top: 30px; background: var(--card-light); }
  .card--back { top: 552px; background: var(--card-dark); }

  /* brand lockup */
  .brand { position: absolute; display: flex; align-items: center; gap: 12px; }
  .brand__dot { border-radius: 50%; background: var(--green); flex: none; }
  .brand__name { color: var(--green); font-weight: 700; }
  .card--front .brand { left: 130px; top: 210px; }
  .card--front .brand__dot { width: 26px; height: 26px; }
  .card--front .brand__name { font-size: 38px; }
  .card--back .brand { left: 0; right: 0; top: 190px; justify-content: center; }
  .card--back .brand__dot { width: 34px; height: 34px; }
  .card--back .brand__name { font-size: 54px; }

  .divider {
    position: absolute; left: 372px; top: 120px; width: 1px; height: 218px;
    background: var(--divider);
  }
  .contact { position: absolute; left: 396px; top: 120px; color: var(--ink); }
  .contact__name { font-size: 30px; font-weight: 700; color: var(--green); line-height: 36px; }
  .contact__role { font-size: 20px; color: var(--ink-soft); line-height: 24px; }
  .contact__address { margin-top: 12px; font-size: 20px; line-height: 25px; }
  .contact__list { list-style: none; margin-top: 12px; font-size: 20px; line-height: 25.5px; }
  .contact__list li { display: flex; align-items: center; gap: 8px; }
  .contact__list svg { width: 18px; height: 18px; flex: none; }

  .band { position: absolute; left: 0; bottom: 0; width: 800px; height: 22px; }

  .services {
    position: absolute; left: 0; right: 0; top: 398px;
    display: flex; justify-content: center; align-items: center; gap: 11px;
    color: var(--white); font-size: 17.5px;
  }
  .services__dot { width: 9px; height: 9px; border-radius: 50%; background: var(--green-bright); }
</style>
</head>
<body>
<main class="canvas">
  <section class="card card--front" aria-label="Business card front">
    <div class="brand">
      <span class="brand__dot"></span>
      <span class="brand__name">Korvane</span>
    </div>
    <div class="divider"></div>
    <div class="contact">
      <h1 class="contact__name">Dalen Ostrow</h1>
      <p class="contact__role">Owner</p>
      <p class="contact__address">214 W. Orchard St.<br>Marlow, OH 45901</p>
      <ul class="contact__list">
        <li>
          <svg viewBox="0 0 24 24"><path fill="#4a9a25" d="M6.6 10.8a15.2 15.2 0 0 0 6.6 6.6l2.2-2.2a1 1 0 0 1 1-.25 11.4 11.4 0 0 0 3.6.57 1 1 0 0 1 1 1V20a1 1 0 0 1-1 1A17 17 0 0 1 3 4a1 1 0 0 1 1-1h3.5a1 1 0 0 1 1 1c0 1.25.2 2.45.57 3.57a1 1 0 0 1-.25 1z"/></svg>
          419-555-0142
        </li>
        <li>
          <svg viewBox="0 0 24 24"><rect x="2" y="5" width="20" height="14" rx="1.5" fill="#4a9a25"/><path d="M3 6.5l9 6.5 9-6.5" fill="none" stroke="#f6f6f6" stroke-width="1.8"/></svg>
          korvanesky@mail.com
        </li>
        <li>
          <svg viewBox="0 0 24 24"><circle cx="12" cy="12" r="10" fill="#4a9a25"/><path d="M8 6c2 1 1 3 3 4s0 3 2 4M15 5c-1 2 1 3 3 3M14 18c1-2 3-2 4-1" fill="none" stroke="#f6f6f6" stroke-width="1.6"/></svg>
          www.korvaneskyworks.com
        </li>
      </ul>
    </div>
    <svg class="band" viewBox="0 0 800 22" preserveAspectRatio="none" aria-hidden="true">
      <defs>
        <linearGradient id="bandGreen" x1="0" x2="1">
          <stop offset="0" stop-color="#1f7a12"/>
          <stop offset="0.55" stop-color="#5f9f2e"/>
          <stop offset="1" stop-color="#1f7a12"/>
        </linearGradient>
      </defs>
      <polygon points="0,0 524,0 517,22 0,22" fill="url(#bandGreen)"/>
      <polygon points="529,0 800,0 800,22 522,22" fill="#000"/>
    </svg>
  </section>

  <section class="card card--back" aria-label="Business card back">
    <div class="brand">
      <span class="brand__dot"></span>
      <span class="brand__name">Korvane</span>
    </div>
    <div class="services">
      <span>Thermal Image Inspections</span><span class="services__dot"></span>
      <span>Deer Recovery</span><span class="services__dot"></span>
      <span>Search&amp; Rescue</span><span class="services__dot"></span>
      <span>Real Estate Photography</span>
    </div>
  </section>
</main>
</body>
</html>
```